Media Services Start-up -- Corporate Website and Logo Design. Inspiration required!

We need a logo design and corporate website design, including coding, for our start-up business.
Brenvora’s value proposition is based on bringing together media content from a vast number of geographies globally, adding human and AI curation, translation and editing, and delivering the content using tailored customer interfaces. On the one hand, the business brings together media coverage from all over the world, and on the other it brings together content, human skills and technology to deliver a supreme customer experience.
Brenvora is a B2B media monitoring and analytics business with emphasis on global customers. Brenvora's service offering is centred around sourcing media content from different markets, processing, storing and delivering the content and insights derived from it using an online platform / mobile app.
The messaging we want to create through the logo is:
- Global scope
- Speed of delivery
- Cost-efficiency
- Multi-lingual
- Tailor-made
- Trustworthy
Target Market(s)
Business to business, PR / Communications, Media, Marketing
Logo Text
Brenvora
Coding
Coded - Design and coding required
Number of Pages Required
5+ page
Font styles to use
Other font styles liked:
- See Design Brief for details
Colors
Designer to choose colors to be used in the design.

```html
<!DOCTYPE html>
<html lang="en">
<head>
<meta charset="utf-8">
<title>Brenvora — Our people</title>
<link rel="stylesheet" href="https://fonts.googleapis.com/css2?family=Questrial&family=Mulish:wght@400;600;700&display=swap">
<style>
  :root {
    --sky: #65b0ec;
    --sky-deep: #2f4f6e;
    --orange: #f26d21;
    --ink: #111111;
    --muted: #8a8a8a;
    --faint: #bdbdbd;
    --panel: #f1f1f1;
    --navy: #041333;
    --cyan: #1aa8e8;
    --ring: #464c63;
    --yellow: #ebbb15;
    --green: #42b45c;
    --violet: #7582bd;
    --white: #ffffff;
  }
  * { margin: 0; padding: 0; box-sizing: border-box; }
  html, body { width: 1044px; height: 1200px; overflow: hidden; background: var(--white); }
  body { position: relative; font-family: "Mulish", sans-serif; color: var(--ink); }
  .abs { position: absolute; }
  .heading { font-family: "Questrial", sans-serif; font-weight: 400; }

  .hero-band { left: 0; top: 0; width: 1044px; height: 260px; }
  .call-line { left: 590px; top: 12px; width: 209px; text-align: right; font-size: 8.5px; color: var(--white); font-weight: 600; white-space: nowrap; }
  .learn-btn { left: 811px; top: 7px; width: 84px; height: 22px; background: var(--orange); border-radius: 2px; color: var(--ink); font-size: 8.5px; display: flex; align-items: center; justify-content: center; gap: 4px; }
  .main-nav { top: 50px; left: 508px; display: flex; gap: 27px; font-size: 10px; color: var(--white); font-family: "Questrial", sans-serif; white-space: nowrap; }
  .page-title { top: 140px; left: 0; width: 1044px; text-align: center; font-size: 31px; color: var(--white); }

  .portrait { left: 135px; top: 260px; width: 102px; height: 102px; background: #efefef; }
  .person-name { left: 327px; top: 292px; font-size: 24px; }
  .person-role { left: 327px; top: 323px; font-size: 9px; letter-spacing: 3px; color: var(--muted); }
  .person-bio { left: 135px; top: 378px; font-size: 10px; color: var(--faint); white-space: nowrap; }
  .social { left: 139px; top: 422px; display: flex; gap: 14px; }
  .social a { width: 12px; height: 12px; display: block; }
  .social svg { width: 12px; height: 12px; display: block; }

  .values { left: 0; top: 460px; width: 1044px; height: 466px; background: var(--panel); }
  .value { text-align: center; }
  .value h3 { font-family: "Questrial", sans-serif; font-weight: 400; font-size: 16px; line-height: 1; margin-bottom: 6px; }
  .value p { font-size: 9.5px; color: var(--muted); line-height: 16px; }
  .v-staff { left: 322px; top: 504px; width: 400px; }
  .v-expertise { left: 322px; top: 815px; width: 400px; }
  .v-capabilities { left: 163px; top: 670px; width: 200px; }
  .v-knowledge { left: 680px; top: 652px; width: 200px; }
  .cycle { left: 0; top: 0; width: 1044px; height: 1200px; }

  .site-footer { left: 0; top: 926px; width: 1044px; height: 274px; background: var(--navy); color: var(--white); }
  .foot-col { top: 35px; font-family: "Questrial", sans-serif; }
  .foot-col h4 { font-weight: 400; font-size: 10px; color: var(--cyan); margin-bottom: 24px; }
  .foot-col li { list-style: none; font-size: 11px; line-height: 20.5px; white-space: nowrap; }
  .col-brand { left: 148px; }
  .col-solutions { left: 406px; }
  .col-tech { left: 665px; width: 215px; }
  .col-tech li { line-height: 17px; margin-bottom: 3.5px; white-space: normal; }
  .col-brand svg { vertical-align: -1px; margin-right: 3px; }
  .foot-rule { left: 148px; top: 219px; width: 748px; height: 1px; background: #24324f; }
  .copyright { left: 0; top: 235px; width: 1044px; text-align: center; font-size: 8.5px; font-weight: 700; }
</style>
</head>
<body>

<svg class="abs hero-band" viewBox="0 0 1044 260" aria-hidden="true">
  <defs>
    <linearGradient id="heroShade" x1="0" y1="0" x2="1" y2="1">
      <stop offset="0" stop-color="#5a9fd8"/>
      <stop offset="0.12" stop-color="#65b0ec"/>
      <stop offset="0.85" stop-color="#65b0ec"/>
      <stop offset="1" stop-color="#2f4f6e"/>
    </linearGradient>
  </defs>
  <polygon points="0,0 1044,0 1044,256 0,192" fill="url(#heroShade)"/>
</svg>

<div class="abs call-line">Call us on: +(61) 02 5550 1947</div>
<div class="abs learn-btn">Learn more
  <svg width="7" height="7" viewBox="0 0 10 10"><circle cx="5" cy="5" r="4" fill="none" stroke="#111" stroke-width="1.4"/><path d="M3.5 5h3M5 3.5 6.5 5 5 6.5" fill="none" stroke="#111" stroke-width="1.2"/></svg>
</div>
<nav class="abs main-nav"><span>Home</span><span>Solutions</span><span>How We Do It</span><span>Our People</span><span>Our Technology</span></nav>
<h1 class="abs page-title heading">Our people</h1>

<div class="abs portrait" role="img" aria-label="Portrait photo of the team member"></div>
<h2 class="abs person-name heading">Mara Ellison</h2>
<div class="abs person-role">CEO</div>
<p class="abs person-bio">Lorem ipsum dolor sit amet, consectetur adipiscing elit. Ut elit tellus, luctus nec ullamcorper mattis, pulvinar dapibus leo.</p>
<div class="abs social">
  <a aria-label="Professional profile"><svg viewBox="0 0 12 12"><circle cx="3" cy="6" r="1.8" fill="#111"/><circle cx="9.5" cy="2.5" r="1.8" fill="#111"/><circle cx="9.5" cy="9.5" r="1.8" fill="#111"/><path d="M3 6 9.5 2.5M3 6l6.5 3.5" stroke="#111" stroke-width="1.2"/></svg></a>
  <a aria-label="Community page"><svg viewBox="0 0 12 12"><path d="M1 1.5h10v7H5L2.5 11V8.5H1Z" fill="#111"/></svg></a>
  <a aria-label="Updates feed"><svg viewBox="0 0 12 12"><circle cx="2.2" cy="9.8" r="1.5" fill="#111"/><path d="M1 5.5a5.5 5.5 0 0 1 5.5 5.5M1 1.5A9.5 9.5 0 0 1 10.5 11" fill="none" stroke="#111" stroke-width="1.6"/></svg></a>
</div>

<section class="abs values"></section>
<svg class="abs cycle" viewBox="0 0 1044 1200" aria-hidden="true">
  <g fill="none" stroke="var(--ring)" stroke-width="6" stroke-linecap="round">
    <path d="M522 588 A97 97 0 0 0 425 680"/>
    <path d="M437 737 A97 97 0 0 0 562 777"/>
    <path d="M617 702 A97 97 0 0 0 573 603"/>
  </g>
  <circle cx="522" cy="588" r="23.5" fill="var(--yellow)"/>
  <circle cx="608" cy="734" r="23.5" fill="var(--green)"/>
  <circle cx="435" cy="734" r="23.5" fill="var(--violet)"/>
</svg>
<div class="abs value v-staff"><h3>OUR STAFF</h3><p>Lorem ipsum dolor sit amet, consectetur adipiscing elit.</p></div>
<div class="abs value v-capabilities"><h3>CAPABILITIES</h3><p>Lorem ipsum dolor sit amet, consectetur adipiscing elit.</p></div>
<div class="abs value v-knowledge"><h3>KNOWLEDGE</h3><p>Lorem ipsum dolor sit amet, consectetur adipiscing elit.</p></div>
<div class="abs value v-expertise"><h3>EXPERTISE</h3><p>Lorem ipsum dolor sit amet, consectetur adipiscing elit.</p></div>

<footer class="abs site-footer">
  <div class="abs foot-col col-brand">
    <h4>BRENVORA</h4>
    <ul>
      <li><svg width="7" height="10" viewBox="0 0 7 10"><path d="M3.5 0A3.5 3.5 0 0 0 0 3.5C0 6 3.5 10 3.5 10S7 6 7 3.5A3.5 3.5 0 0 0 3.5 0Zm0 5a1.5 1.5 0 1 1 0-3 1.5 1.5 0 0 1 0 3Z" fill="#fff"/></svg>48 Harlow Street, Westbridge, WB 20417.</li>
      <li><svg width="9" height="9" viewBox="0 0 10 10"><path d="M2 0 4 2.5 3 4c.7 1.3 1.7 2.3 3 3l1.5-1L10 8 8.5 10C4 9.6.4 6 0 1.5Z" fill="#fff"/></svg>555.019283</li>
      <li><svg width="11" height="9" viewBox="0 0 11 9"><rect x=".6" y=".6" width="9.8" height="7.8" fill="none" stroke="#fff" stroke-width="1.2"/><path d="M.6.8 5.5 5 10.4.8" fill="none" stroke="#fff" stroke-width="1.2"/></svg>info@brenvora.com</li>
    </ul>
  </div>
  <div class="abs foot-col col-solutions">
    <h4>SOLUTIONS</h4>
    <ul>
      <li>Content Sourcing</li>
      <li>Content Collection</li>
      <li>Content Augmentation</li>
      <li>Content Delivery</li>
      <li>Media Insights &amp; Consultancy</li>
    </ul>
  </div>
  <div class="abs foot-col col-tech">
    <h4>OUR TECHNOLOGY</h4>
    <ul>
      <li>Content Ingestion / Normalisation &amp; Augmentation</li>
      <li>Content Delivery</li>
      <li>Insight Services</li>
    </ul>
  </div>
  <div class="abs foot-rule"></div>
  <div class="abs copyright">© 2019 Brenvora</div>
</footer>

</body>
</html>
```